Roll-up BETON IMPRIME

(Title): BETON IMPRIME
(Catch phrase): Des sols uniques
(Bullet points):
Aménagements urbains
Terrasses
Parcs à thèmes
Plages Piscines
Allées
Grand nombre de couleurs et textures...des milliers de possibilités
Our logo (SOLIDE FACTURE ...) well visible.
BRVN Logo (small at the bottom of the roll-up somewhere with a small text right on top of logo saying: "Classement performanciel". Just to hve it, but not part of the main design.
Picture BE Rond point needs to be zoomed a little to better show texture
Picture DSCN: cut out the ugly fence + left jobsite vision
Picture formation: cross out and state: "Fini les pavés qui déchaussent !"
(just fyi so you understand the comment while doing the design; because our solution makes a monolythic slab that cannot lift).
Roll-up is going to be used in show-rooms to explain what stamped concrete is about. We need something classy and modern.
Dimension of roll-up image: 85.2x220.2:
Good luck
Target Market(s)
architects, homeowners, contractors
Industry/Entity Type
Concrete
Look and feel

```html
<!DOCTYPE html>
<html lang="fr">
<head>
<meta charset="utf-8">
<title>Roll-up Béton Imprimé – Solide Facture</title>
<link rel="stylesheet" href="https://fonts.googleapis.com/css2?family=Arimo:wght@400;700&family=PT+Sans+Narrow:wght@400;700&display=swap">
<style>
  :root {
    --page: #ececec;
    --panel-top: #f1f1f1;
    --panel-bottom: #e2e2e2;
    --brand-blue: #1f5fae;
    --deep-blue: #164a93;
    --pale-blue: #2f6fc0;
    --ink: #454545;
    --soft-ink: #666;
    --rule: #c9c9c9;
    --tag-grey: #5b5b5b;
    --tag-green: #16965a;
    --tag-lime: #27a046;
    --tag-blue: #1d5aa9;
    --tag-orange: #ef8a17;
    --alert-red: #d3232a;
  }
  * { box-sizing: border-box; margin: 0; padding: 0; }
  html, body { width: 1170px; height: 1200px; overflow: hidden; background: var(--page); }

  .rollup {
    position: absolute; left: 362px; top: 24px;
    width: 446px; height: 1152px; overflow: hidden;
    background: linear-gradient(180deg, var(--panel-top), var(--panel-bottom));
    box-shadow: 0 4px 18px rgba(0,0,0,.18);
    font-family: "PT Sans Narrow", "Arial Narrow", sans-serif;
  }
  .abs { position: absolute; }

  /* brand pennant */
  .pennant {
    left: 65px; top: 0; width: 292px; height: 137px;
    background: #fff;
    clip-path: polygon(0 0, 100% 0, 100% 84%, 50% 100%, 0 84%);
    text-align: center; padding-top: 40px;
  }
  .brand-name {
    font-family: "Arimo", Arial, sans-serif; font-weight: 700;
    font-size: 28px; color: var(--brand-blue); letter-spacing: .5px;
  }
  .brand-tagline {
    font-family: "Arimo", Arial, sans-serif; font-weight: 700;
    font-size: 15px; color: #6e6e6e; margin-top: 2px;
  }

  /* headline */
  .headline {
    left: 63px; top: 150px; width: 330px;
    font-family: "Arimo", Arial, sans-serif; font-weight: 700;
    font-size: 74px; line-height: 64px; color: var(--brand-blue);
    letter-spacing: -1px;
  }
  .colour-dot {
    left: 318px; top: 160px; width: 36px; height: 36px; border-radius: 50%;
    background: conic-gradient(#e63b2e, #f39a1b, #f4d21f, #3bb34a, #1f5fae, #8e3fa5, #e63b2e);
  }
  .subline {
    left: 63px; top: 298px; width: 314px; text-align: center;
    font-family: "Arimo", Arial, sans-serif; font-size: 13px;
    letter-spacing: 7px; color: var(--soft-ink); text-transform: uppercase;
  }
  .rule { left: 0; width: 446px; height: 2px; background: var(--rule); }
  .rule-top { top: 332px; }
  .rule-mid { top: 428px; }

  .catchphrase {
    left: 0; top: 352px; width: 446px; text-align: center;
    font-weight: 700; font-size: 25px; line-height: 32px; color: var(--ink);
  }

  .gallery { left: 0; top: 436px; }

  /* application tags */
  .tag {
    height: 36px; line-height: 36px; color: #fff;
    font-weight: 700; font-size: 23px; text-align: center;
  }
  .tag-urban  { left: 0;   top: 868px; width: 250px; background: var(--tag-grey);  clip-path: polygon(0 0, 94% 0, 100% 50%, 94% 100%, 0 100%); }
  .tag-parks  { left: 268px; top: 868px; width: 178px; background: var(--tag-green); clip-path: polygon(0 0, 100% 0, 100% 100%, 0 100%, 6% 50%); }
  .tag-terrace{ left: 0;   top: 914px; width: 125px; background: var(--tag-lime);  clip-path: polygon(0 0, 90% 0, 100% 50%, 90% 100%, 0 100%); }
  .tag-pool   { left: 140px; top: 914px; width: 191px; background: var(--tag-blue); clip-path: polygon(6% 0, 94% 0, 100% 50%, 94% 100%, 6% 100%, 0 50%); }
  .tag-paths  { left: 349px; top: 914px; width: 97px;  background: var(--tag-orange); clip-path: polygon(10% 0, 100% 0, 100% 100%, 10% 100%, 0 50%); }

  .divider { left: 0; top: 972px; }

  /* before / after */
  .proof { left: 0; top: 990px; }
  .proof-text {
    left: 130px; top: 1010px; width: 190px; text-align: center;
    font-size: 27px; line-height: 32px; color: var(--ink);
  }

  .cert-label {
    left: 350px; top: 1086px; width: 90px; text-align: right;
    font-family: "Arimo", Arial, sans-serif; font-size: 5.5px; color: #666; text-transform: uppercase;
  }
  .cert-name {
    left: 350px; top: 1093px; width: 86px; text-align: right;
    font-family: "PT Sans Narrow", sans-serif; font-weight: 700;
    font-size: 20px; color: var(--deep-blue);
  }

  .footer-wave { left: 0; top: 1104px; }
</style>
</head>
<body>
<main class="rollup">

  <header class="pennant abs">
    <div class="brand-name">SOLIDE FACTURE</div>
    <div class="brand-tagline">100% béton décoratif</div>
  </header>

  <h1 class="headline abs">BETON<br>IMPRIMÉ</h1>
  <div class="colour-dot abs" role="img" aria-label="Nuancier de couleurs"></div>
  <p class="subline abs">Des sols uniques</p>

  <div class="rule rule-top abs"></div>
  <p class="catchphrase abs">Grand nombre de couleurs et textures...<br>des milliers de possibilités</p>
  <div class="rule rule-mid abs"></div>

  <svg class="gallery abs" width="446" height="410" viewBox="0 436 446 410">
    <rect x="0" y="436" width="446" height="410" fill="#fff"/>
    <defs>
      <linearGradient id="g-pool" x1="0" y1="0" x2="0" y2="1">
        <stop offset="0" stop-color="#3f8fb4"/><stop offset=".3" stop-color="#8a7a62"/><stop offset="1" stop-color="#6d5d48"/>
      </linearGradient>
      <linearGradient id="g-deck" x1="0" y1="0" x2="1" y2="1">
        <stop offset="0" stop-color="#5a86a8"/><stop offset="1" stop-color="#3d5670"/>
      </linearGradient>
      <linearGradient id="g-round" x1="0" y1="0" x2="0" y2="1">
        <stop offset="0" stop-color="#7a8a6a"/><stop offset=".45" stop-color="#9a5a44"/><stop offset="1" stop-color="#5e5e5e"/>
      </linearGradient>
      <linearGradient id="g-mat" x1="0" y1="0" x2="1" y2="1">
        <stop offset="0" stop-color="#e9c21f"/><stop offset=".45" stop-color="#d8752a"/><stop offset="1" stop-color="#c0602a"/>
      </linearGradient>
    </defs>
    <polygon points="0,440 190,440 222,636 0,650" fill="url(#g-pool)" role="img" aria-label="Plage de piscine en béton imprimé avec rose des vents"/>
    <polygon points="198,440 446,440 446,620 230,636" fill="url(#g-deck)" role="img" aria-label="Terrasse en béton imprimé imitation bois"/>
    <polygon points="0,658 222,644 240,844 0,844" fill="url(#g-round)" role="img" aria-label="Rond-point en béton imprimé rouge avec arbre central"/>
    <polygon points="230,644 446,628 446,844 248,844" fill="url(#g-mat)" role="img" aria-label="Matrice d'impression jaune posée sur béton orange"/>
  </svg>

  <div class="tag tag-urban abs">Aménagements urbains</div>
  <div class="tag tag-parks abs">Parcs à thèmes</div>
  <div class="tag tag-terrace abs">Terrasses</div>
  <div class="tag tag-pool abs">Plage piscines</div>
  <div class="tag tag-paths abs">Allées</div>

  <svg class="divider abs" width="446" height="16" viewBox="0 0 446 16">
    <polyline points="0,4 208,4 223,14 238,4 446,4" fill="none" stroke="#c9c9c9" stroke-width="2"/>
  </svg>

  <svg class="proof abs" width="446" height="100" viewBox="0 990 446 100">
    <rect x="18" y="996" width="77" height="84" fill="#c9b48c" role="img" aria-label="Pavés soulevés"/>
    <rect x="19" y="997" width="75" height="82" fill="none" stroke="var(--alert-red)" stroke-width="2.5"/>
    <line x1="19" y1="997" x2="94" y2="1079" stroke="var(--alert-red)" stroke-width="2.5"/>
    <path d="M106,1034 l9,6 l-9,6 z" fill="#555"/>
    <path d="M316,1034 l9,6 l-9,6 z" fill="#555"/>
    <rect x="333" y="996" width="78" height="84" fill="#7b7f86" role="img" aria-label="Dalle monolithique en béton imprimé"/>
    <rect x="333" y="996" width="78" height="84" fill="none" stroke="#fff" stroke-width="2"/>
  </svg>
  <p class="proof-text abs">Fini les pavés<br>qui déchaussent !</p>

  <div class="cert-label abs">Classement performanciel</div>
  <div class="cert-name abs">BRVN</div>

  <svg class="footer-wave abs" width="446" height="48" viewBox="0 1104 446 48">
    <polygon points="80,1140 223,1108 366,1140" fill="var(--pale-blue)"/>
    <rect x="0" y="1140" width="446" height="12" fill="var(--deep-blue)"/>
  </svg>

</main>
</body>
</html>
```